Reaching the Root: Reasoning in Clinical Choice-Making

I'd like a cover that looks like it would fit on the shelf next to "The Symptom Mirage" by Harold Vintner, "The Fall of Forgetting" by Carl Mortenson, "Meal Mend" by Neil Forsby, "The Energy Renewal Plan" by Owen Prichardson or "The Gland Renewal Plan" by the same or "The Cortex Renewal Plan" by the same ... either text only (with some interesting fonts that make the title stand out, and the subtitle smaller) or a relevant image, though I'm not entirely sure what that would be since this is a book about big-picture medical decision making.
Author name is Dr Miriam Oakhurst, NMD
I'll eventually request an e-book, paperback, and audio cover from the winner...

Target Market(s)

practicing physicians

Industry/Entity Type

medicine

Requirements
Must have
• look similar to other books in the genre

```html
<!DOCTYPE html>
<html lang="en">
<head>
<meta charset="utf-8">
<title>Reaching the Root — Book Cover</title>
<link rel="stylesheet" href="https://fonts.googleapis.com/css2?family=Oswald:wght@500;600&family=Montserrat:wght@500&family=EB+Garamond:ital,wght@0,400;1,400&family=Barlow+Condensed:wght@500;600&display=swap">
<style>
  :root {
    --backdrop: #9b9b9b;
    --paper: #f8f8f6;
    --navy: #0f2140;
    --gold: #b8880f;
    --gold-line: #c29a35;
  }
  * { margin: 0; padding: 0; box-sizing: border-box; }
  html, body {
    width: 1200px;
    height: 1200px;
    overflow: hidden;
    background: var(--backdrop);
  }
  .cover {
    position: absolute;
    left: 200px;
    top: 0;
    width: 800px;
    height: 1200px;
    background: var(--paper);
    color: var(--navy);
  }
  .title-top {
    position: absolute;
    top: 132px;
    left: 0;
    width: 100%;
    text-align: center;
    font-family: "Oswald", sans-serif;
    font-weight: 600;
    font-size: 112px;
    line-height: 1;
    letter-spacing: 3px;
    color: var(--navy);
  }
  .title-main {
    position: absolute;
    top: 270px;
    left: 0;
    width: 100%;
    text-align: center;
    font-family: "Montserrat", sans-serif;
    font-weight: 500;
    font-size: 232px;
    line-height: 1;
    letter-spacing: -4px;
    color: var(--gold);
  }
  .subtitle {
    position: absolute;
    top: 530px;
    left: 0;
    width: 100%;
    text-align: center;
    font-family: "EB Garamond", serif;
    color: var(--navy);
  }
  .subtitle-lead {
    display: flex;
    align-items: center;
    justify-content: center;
    gap: 26px;
    font-style: italic;
    font-size: 38px;
    line-height: 1.1;
  }
  .subtitle-lead .rule {
    width: 150px;
    height: 1.5px;
    background: var(--gold-line);
  }
  .subtitle-main {
    font-size: 40px;
    line-height: 1.3;
  }
  .emblem {
    position: absolute;
    left: 222px;
    top: 650px;
    width: 356px;
    height: 356px;
    border-radius: 50%;
    background: radial-gradient(circle, #f8f8f6 52%, #c9cfdb 62%, #1f3257 72%, #f8f8f6 74%);
  }
  .diagram {
    position: absolute;
    left: 0;
    top: 0;
    width: 800px;
    height: 1200px;
  }
  .label {
    position: absolute;
    font-family: "Barlow Condensed", sans-serif;
    font-weight: 500;
    font-size: 19px;
    line-height: 1.3;
    letter-spacing: 2.5px;
    text-align: center;
    color: var(--navy);
  }
  .label-questions { left: 44px; top: 760px; width: 160px; }
  .label-decisions { left: 598px; top: 760px; width: 160px; }
  .label-outcomes { left: 320px; top: 1014px; width: 160px; }
  .footer-rule {
    position: absolute;
    left: 95px;
    top: 1102px;
    width: 610px;
    height: 1.5px;
    background: var(--gold-line);
  }
  .author {
    position: absolute;
    top: 1122px;
    left: 0;
    width: 100%;
    text-align: center;
    font-family: "Barlow Condensed", sans-serif;
    font-weight: 600;
    font-size: 37px;
    line-height: 1;
    letter-spacing: 6px;
    color: var(--navy);
  }
</style>
</head>
<body>
  <main class="cover">
    <h1>
      <span class="title-top">REACHING THE</span>
      <span class="title-main">ROOT</span>
    </h1>
    <div class="subtitle">
      <p class="subtitle-lead"><span class="rule"></span>Reasoning in<span class="rule"></span></p>
      <p class="subtitle-main">Clinical Choice-Making</p>
    </div>

    <div class="emblem" role="img" aria-label="Compass rose inside a navy brush-stroke circle"></div>

    <svg class="diagram" viewBox="0 0 800 1200" aria-hidden="true">
      <g stroke="#c29a35" stroke-width="1.5" fill="#c29a35">
        <line x1="186" y1="782" x2="244" y2="782"/>
        <circle cx="186" cy="782" r="3.5"/>
        <circle cx="244" cy="782" r="3.5"/>
        <line x1="556" y1="782" x2="614" y2="782"/>
        <circle cx="556" cy="782" r="3.5"/>
        <circle cx="614" cy="782" r="3.5"/>
        <line x1="400" y1="938" x2="400" y2="1004"/>
        <circle cx="400" cy="1006" r="3.5"/>
      </g>
    </svg>

    <p class="label label-questions">BETTER<br>QUESTIONS</p>
    <p class="label label-decisions">BETTER<br>DECISIONS</p>
    <p class="label label-outcomes">BETTER<br>OUTCOMES</p>

    <div class="footer-rule"></div>
    <p class="author">DR MIRIAM OAKHURST, NMD</p>
  </main>
</body>
</html>
```